Recruitment Poster KSE and KPE

Need a poster for new singers : for the Karsel Singing Ensemble and for our new initiative Karsel Petite Ensemble. The target audience for the Youth Choir is young teens (13-18) and for the Junior Choir is parents of kids aged 7-10. Both choirs need to appeal more to boys as girls are more easily recruited into choir.

Industry/Entity Type

Recruitment

```html
<!DOCTYPE html>
<html lang="en">
<head>
<meta charset="utf-8">
<title>Karsel Singing Ensemble – Recruitment Poster</title>
<link rel="stylesheet" href="https://fonts.googleapis.com/css2?family=League+Gothic&family=Jost:wght@400;500;600&display=swap">
<style>
  :root {
    --backdrop: #e6e6e4;
    --paper: #ffffff;
    --red: #e0262c;
    --red-dark: #a81a1f;
    --ink: #111111;
    --black: #0d0d0d;
    --link-blue: #8fb4ff;
  }
  * { box-sizing: border-box; margin: 0; padding: 0; }
  html, body { width: 1200px; height: 1148px; overflow: hidden; }
  body { background: var(--backdrop); position: relative; }

  .poster {
    position: absolute; left: 210px; top: 20px;
    width: 780px; height: 1108px;
    background: var(--paper);
    overflow: hidden;
    box-shadow: 0 2px 10px rgba(0,0,0,0.12);
  }

  .choir-photo {
    position: absolute; left: 0; top: 0; width: 780px; height: 460px;
    background: linear-gradient(180deg, #cfcfcf 0%, #b4b4b4 22%, #6a6a6a 42%, #4a4a4a 70%, #202020 100%);
  }

  .brand {
    position: absolute; right: 64px; top: 48px;
    text-align: right; color: var(--ink);
    font-family: "Jost", sans-serif;
  }
  .brand-name {
    display: flex; align-items: center; justify-content: flex-end; gap: 8px;
    font-weight: 500; font-size: 34px; letter-spacing: 1px; line-height: 1;
  }
  .brand-dot { width: 14px; height: 14px; border-radius: 50%; background: var(--red); }
  .brand-sub { font-size: 12px; font-weight: 500; letter-spacing: 0.5px; margin-top: 4px; }

  .headline-band {
    position: absolute; left: 0; top: 460px; width: 780px; height: 163px;
    background: var(--red);
    display: flex; align-items: center; justify-content: center;
  }
  .headline {
    font-family: "League Gothic", sans-serif; font-weight: 400;
    font-size: 104px; line-height: 1; color: var(--ink);
    text-transform: uppercase; white-space: nowrap; letter-spacing: 0.5px;
    padding-top: 6px;
  }

  .line {
    position: absolute; left: 0; width: 780px;
    text-align: center; white-space: nowrap; text-transform: uppercase;
  }
  .invite {
    top: 642px;
    font-family: "League Gothic", sans-serif;
    font-size: 44px; line-height: 1.05; color: var(--red);
  }
  .call-out {
    top: 744px;
    font-family: "League Gothic", sans-serif;
    font-size: 66px; line-height: 1; color: var(--ink);
  }
  .ribbon {
    position: absolute; left: 90px; top: 818px; width: 600px; height: 60px;
  }
  .ribbon svg { position: absolute; left: 0; top: 0; }
  .ribbon-text {
    position: absolute; left: 0; right: 0; top: 6px; text-align: center;
    font-family: "Jost", sans-serif; font-weight: 500;
    font-size: 26px; line-height: 36px; color: #fff; letter-spacing: 0.5px;
    text-transform: uppercase; white-space: nowrap;
  }
  .junior-line {
    top: 898px;
    font-family: "Jost", sans-serif; font-weight: 600;
    font-size: 18px; line-height: 1.2; color: var(--ink);
  }

  .contact-bar {
    position: absolute; left: 0; top: 956px; width: 780px; height: 152px;
    background: var(--black); color: #fff;
    font-family: "Jost", sans-serif; font-weight: 400;
    font-size: 22px; line-height: 1.35; text-transform: uppercase;
    text-align: center; padding-top: 24px; white-space: nowrap;
  }
  .social { color: var(--link-blue); }
</style>
</head>
<body>
  <main class="poster">
    <div class="choir-photo" role="img" aria-label="Black and white photograph of a youth choir in white shirts and dark uniforms singing on stage"></div>

    <div class="brand">
      <div class="brand-name">KARSEL <span class="brand-dot"></span></div>
      <div class="brand-sub">YOUTH &amp; PETITE ENSEMBLES</div>
    </div>

    <section class="headline-band">
      <h1 class="headline">Calling Young Singers</h1>
    </section>

    <p class="line invite">If you are aged 11-18, can sing and want to<br>come on tour to Germany next March-April 2016</p>
    <p class="line call-out">Karsel Singing Ensemble needs you</p>
    <div class="ribbon">
      <svg width="600" height="60" viewBox="0 0 600 60" aria-hidden="true">
        <polygon points="0,18 62,18 62,60 0,60 16,39" fill="var(--red)"/>
        <polygon points="600,18 538,18 538,60 600,60 584,39" fill="var(--red)"/>
        <polygon points="42,48 62,60 62,48" fill="var(--red-dark)"/>
        <polygon points="558,48 538,60 538,48" fill="var(--red-dark)"/>
        <rect x="42" y="0" width="516" height="48" fill="var(--red)"/>
      </svg>
      <div class="ribbon-text">Starting September 2015...</div>
    </div>
    <p class="line junior-line">Karsel Petite Ensemble for young singers aged 7–10 years</p>

    <footer class="contact-bar">
      <p>For more information email info@karselsinging.org</p>
      <p>See www.karselsinging.org <span class="social">Like us on Friendbook</span></p>
    </footer>
  </main>
</body>
</html>
```